I need business cards for a company that will be an umbrella for many retail stores. I need them to be sleek and modern. I would like some white and black in the background of the card as these are the office colours the logo is attached.
Target Market(s)
worldwide
Industry/Entity Type
Business
Requirements
Must have
- traditional business card shape
Should not have
- too many colours
no swirly text

```html
<!DOCTYPE html>
<html lang="en">
<head>
<meta charset="utf-8">
<title>Norvale General Trading – Business Cards</title>
<link rel="stylesheet" href="https://fonts.googleapis.com/css2?family=Open+Sans:wght@400;600&display=swap">
<style>
  :root {
    --backdrop: #e9e6e2;
    --card: #ffffff;
    --brand-blue: #0c5fa9;
    --ink-light: #ffffff;
    --ink-dark: #2f2f33;
    --mark: #7fa6d2;
  }
  * { box-sizing: border-box; margin: 0; padding: 0; }
  html, body { width: 1200px; height: 911px; overflow: hidden; }
  body {
    background: var(--backdrop);
    font-family: "Open Sans", Arial, sans-serif;
    position: relative;
  }
  .card {
    position: absolute;
    width: 776px;
    height: 430px;
    background: var(--card);
  }
  .card--landscape { left: 28px; top: 8px; }
  .card--portrait-logo { left: 398px; top: 474px; }

  .contact-panel {
    position: absolute;
    background: var(--brand-blue);
    color: var(--ink-light);
  }
  .card--landscape .contact-panel {
    left: 0; top: 83px; width: 374px; height: 253px;
    text-align: right;
  }
  .card--portrait-logo .contact-panel {
    left: 215px; top: 89px; width: 474px; height: 241px;
  }
  .contact-name { position: absolute; font-size: 24px; line-height: 1; }
  .contact-email { position: absolute; font-size: 18px; line-height: 1; }
  .contact-line {
    position: absolute;
    display: flex; align-items: center; justify-content: flex-end; gap: 12px;
    font-size: 18px; line-height: 1;
  }
  .contact-line svg { width: 30px; height: 30px; flex: none; }

  .card--landscape .contact-name { right: 24px; top: 14px; }
  .card--landscape .contact-email { right: 24px; top: 46px; }
  .card--landscape .contact-phone { right: 22px; top: 158px; }
  .card--landscape .contact-address { right: 22px; top: 200px; }

  .card--portrait-logo .contact-name { left: 22px; top: 20px; }
  .card--portrait-logo .contact-email { left: 22px; top: 52px; }
  .card--portrait-logo .contact-phone { right: 22px; top: 152px; }
  .card--portrait-logo .contact-address { right: 22px; top: 190px; }

  .brand {
    position: absolute;
    display: flex; align-items: center; gap: 18px;
    color: var(--ink-dark);
  }
  .brand-dot {
    width: 70px; height: 70px; border-radius: 50%;
    background: var(--mark); flex: none;
  }
  .brand-name {
    font-size: 30px; font-weight: 400; line-height: 1.15;
    letter-spacing: 1px;
  }
  .card--landscape .brand { left: 392px; top: 168px; }
  .card--portrait-logo .brand {
    left: 130px; top: 200px;
    transform: translate(-50%, -50%) rotate(-90deg);
    transform-origin: center;
    flex-direction: row-reverse;
  }
</style>
</head>
<body>
  <section class="card card--landscape">
    <div class="contact-panel">
      <p class="contact-name">Your name</p>
      <p class="contact-email">email@yourdomain.com</p>
      <p class="contact-line contact-phone">Your telephone
        <svg viewBox="0 0 24 24" aria-hidden="true"><path fill="#fff" d="M14 3c1 0 2 1 2 2l-2 4c-.4.7-1.4.8-2 .3-.8 1.6-1 3.6-.4 5.4.7-.3 1.6 0 1.9.7l1.6 4c.3.8-.2 1.6-1 1.6-3 0-5-3-5-9s2-9 4.9-9z"/></svg>
      </p>
      <p class="contact-line contact-address">Your Address
        <svg viewBox="0 0 24 24" aria-hidden="true"><path fill="#fff" d="M2 8 12 3l10 5v2H2zM4 11h3v7H4zm6.5 0h3v7h-3zM17 11h3v7h-3zM2 19h20v2H2z"/></svg>
      </p>
    </div>
    <div class="brand">
      <span class="brand-dot"></span>
      <p class="brand-name">Norvale<br>General Trading</p>
    </div>
  </section>

  <section class="card card--portrait-logo">
    <div class="brand">
      <span class="brand-dot"></span>
      <p class="brand-name">Norvale<br>General Trading</p>
    </div>
    <div class="contact-panel">
      <p class="contact-name">Your name</p>
      <p class="contact-email">email@yourdomain.com</p>
      <p class="contact-line contact-phone">Your telephone
        <svg viewBox="0 0 24 24" aria-hidden="true"><path fill="#fff" d="M14 3c1 0 2 1 2 2l-2 4c-.4.7-1.4.8-2 .3-.8 1.6-1 3.6-.4 5.4.7-.3 1.6 0 1.9.7l1.6 4c.3.8-.2 1.6-1 1.6-3 0-5-3-5-9s2-9 4.9-9z"/></svg>
      </p>
      <p class="contact-line contact-address">Your Address
        <svg viewBox="0 0 24 24" aria-hidden="true"><path fill="#fff" d="M2 8 12 3l10 5v2H2zM4 11h3v7H4zm6.5 0h3v7h-3zM17 11h3v7h-3zM2 19h20v2H2z"/></svg>
      </p>
    </div>
  </section>
</body>
</html>
```